Eco friendly Swedish beauty products sold in aluminum bottles - label design needed

We need help in designing a series of stick on labels for 80 ml (2.7 fl. oz.) aluminum bottles containing beauty products such as soaps, shampoo etc. The diameter of the bottle is 36 mm and the body of the bottles measures approx. 106 mm.
It is important for us that the label has a simplistic and clean feel with few colors (and the right ones!) and that the label helps amplify this product being both better and a more sustainable alternative to many of our plastic bottle competitors. The design and label should communicate the feel of an Eco-friendly, sustainable and modern brand of high quality - and with a Swedish concept.
We are using Montserrat font in our materials. Find attached information of preferred colors, the bottles and one example of our logotype. I am also available on e-mail should further information be needed.

Looking forward and very excited to receive your suggestions.
Note that we are expecting to start selling a series of approximately 10 different products where I will need one "master design" and then only smaller changes for each of the different products.

Target Market(s)

People whom are aware and not only look at price tag. Private and commercial market.

Industry/Entity Type

Beauty

Font styles to use
Other font styles liked:
• Montserrat

Requirements
Must have
• It must give the feel of being both better and a more sustainable alternative to many of our plastic bottle competitors.
Nice to have
• Simplistic. Clean. Clear.
Should not have
• Wrong colors, too complex designs.

```html
<!DOCTYPE html>
<html lang="en">
<head>
<meta charset="utf-8">
<title>Body Lotion Label</title>
<link href="https://fonts.googleapis.com/css2?family=Montserrat:wght@400;500;600&display=swap" rel="stylesheet">
<style>
  :root {
    --backdrop: #ededed;
    --label-light: #f7f7f7;
    --label-mid: #ececec;
    --ink: #2a2a2a;
    --ink-soft: #555555;
    --peach: #e2a890;
  }
  html, body {
    margin: 0;
    padding: 0;
    width: 1146px;
    height: 1200px;
    overflow: hidden;
    background: var(--backdrop);
    font-family: "Montserrat", sans-serif;
  }
  .canvas {
    position: relative;
    width: 1146px;
    height: 1200px;
  }
  .label {
    position: absolute;
    left: 413px;
    top: 50px;
    width: 320px;
    height: 1100px;
    background: linear-gradient(90deg, var(--label-mid) 0%, var(--label-light) 45%, var(--label-mid) 100%);
    color: var(--ink);
  }
  .brand {
    position: absolute;
    left: 52px;
    top: 100px;
    height: 470px;
    display: flex;
    align-items: flex-start;
    gap: 10px;
  }
  .brand-name,
  .brand-origin {
    writing-mode: vertical-rl;
    transform: rotate(180deg);
    margin: 0;
    font-weight: 400;
    color: var(--ink);
    white-space: nowrap;
  }
  .brand-name {
    font-size: 40px;
    letter-spacing: 3px;
    line-height: 1;
    height: 470px;
    text-align: left;
  }
  .brand-origin {
    font-size: 13px;
    letter-spacing: 6px;
    line-height: 1;
    color: var(--ink-soft);
    height: 470px;
    text-align: right;
  }
  .brand-dot {
    position: absolute;
    left: 58px;
    top: 600px;
    width: 34px;
    height: 34px;
    border-radius: 50%;
    background: var(--ink);
  }
  .accent-band {
    position: absolute;
    left: 48px;
    top: 688px;
    width: 232px;
    height: 14px;
    background: var(--peach);
  }
  .product {
    position: absolute;
    left: 48px;
    top: 722px;
    right: 20px;
  }
  .product-name {
    margin: 0 0 8px;
    font-size: 34px;
    font-weight: 500;
    letter-spacing: 0.5px;
  }
  .product-detail {
    margin: 0;
    font-size: 18px;
    font-weight: 600;
    line-height: 1.35;
    color: var(--ink-soft);
  }
  .volume {
    position: absolute;
    left: 48px;
    top: 960px;
    margin: 0;
    font-size: 20px;
    font-weight: 500;
    color: var(--ink-soft);
  }
</style>
</head>
<body>
  <main class="canvas">
    <section class="label">
      <div class="brand">
        <p class="brand-name">LUMA BY NORDLIN</p>
        <p class="brand-origin">SWEDEN</p>
      </div>
      <span class="brand-dot" aria-hidden="true"></span>
      <div class="accent-band"></div>
      <div class="product">
        <h1 class="product-name">BODY LOTION</h1>
        <p class="product-detail">With Aloe &amp; Lavender</p>
        <p class="product-detail">For dry skin</p>
      </div>
      <p class="volume">80 ml (2.7 fl. oz.)</p>
    </section>
  </main>
</body>
</html>
```